Tunevia artwork for new single release

I need Tunevia artwork creating to release a new single on there.

The specs are:

Ideal size: 3000 x 3000 pixels
Minimum size: 1400 x 1400 pixels
Aspect ratio: 1:1 (must be a perfect square)
File format: JPG or PNG
Color space: sRGB
File size: Max 4MB

The song is called "Still, Can We Dance?"
The artist is "Milo Brannick"

We have no images of Milo, so it really is open to imagination.

Target Market(s)

Tunevia listeners

Industry/Entity Type

Music

```html
<!DOCTYPE html>
<html lang="en">
<head>
<meta charset="utf-8">
<title>Still, Can We Dance? — Milo Brannick</title>
<link rel="stylesheet" href="https://fonts.googleapis.com/css2?family=Cormorant+Garamond:ital,wght@1,400;1,500&family=Manrope:wght@400&display=swap">
<style>
  :root {
    --page: #ffffff;
    --teal-deep: #173f52;
    --teal: #157a94;
    --teal-light: #1b8fa8;
    --navy: #141a26;
    --heart-red: #c8262a;
    --ink-light: #ffffff;
  }
  * { margin: 0; padding: 0; box-sizing: border-box; }
  html, body {
    width: 828px; height: 1200px; overflow: hidden;
    background: var(--page);
  }
  .canvas {
    position: relative; width: 828px; height: 1200px;
  }
  .cover {
    position: absolute; left: 94px; top: 280px;
    width: 640px; height: 640px; overflow: hidden;
    box-shadow: 0 18px 24px -14px rgba(0,0,0,0.35);
  }
  .cover-art {
    position: absolute; inset: 0;
    background:
      radial-gradient(circle at 82% 72%, var(--heart-red) 0%, rgba(200,38,42,0.85) 18%, rgba(200,38,42,0) 38%),
      radial-gradient(ellipse at 62% 75%, var(--navy) 0%, rgba(20,26,38,0.7) 30%, rgba(20,26,38,0) 55%),
      radial-gradient(circle at 45% 40%, var(--teal-light) 0%, var(--teal) 35%, var(--teal-deep) 85%);
  }
  .title {
    position: absolute; left: 0; top: 0; width: 100%; height: 100%;
    color: var(--ink-light);
    font-family: "Cormorant Garamond", serif;
    font-style: italic; font-weight: 500;
  }
  .title-lead {
    position: absolute; left: 60px; top: 248px;
    font-size: 64px; line-height: 1;
  }
  .title-ring {
    position: absolute; left: 24px; top: 254px;
    width: 190px; height: 84px; overflow: visible;
  }
  .title-main {
    position: absolute; left: 52px; top: 344px;
    font-size: 66px; line-height: 1; white-space: nowrap;
  }
  .artist {
    position: absolute; left: 0; right: 0; top: 566px;
    text-align: center; color: var(--ink-light);
    font-family: "Manrope", sans-serif; font-weight: 400;
    font-size: 32px; letter-spacing: 0.32em;
    padding-left: 0.32em;
  }
</style>
</head>
<body>
  <main class="canvas">
    <section class="cover">
      <div class="cover-art" role="img" aria-label="Illustration of a suited man with dark hair looking down at a large cracked red heart held in his hands, set against a cracked teal mosaic wall"></div>
      <h1 class="title">
        <svg class="title-ring" viewBox="0 0 190 84" aria-hidden="true">
          <ellipse cx="95" cy="42" rx="92" ry="36" transform="rotate(-9 95 42)" fill="none" stroke="#ffffff" stroke-width="1.6"/>
        </svg>
        <span class="title-lead">Still,</span>
        <span class="title-main">Can We Dance?</span>
      </h1>
      <p class="artist">MILO BRANNICK</p>
    </section>
  </main>
</body>
</html>
```